Business card design for a engineering company

I need a double sided business card design for my company "Verdmont Flow Solutions". The card will be used in Malaysia. Sleek and professional, with a little design flare to it.
Information to showcase:
1. Company logo
2. Name, title, phone, email address, website address
3. our products "Pumping technology, Valve & actuation, Air Moving Technology
Example:
Ravi Tanaka
Business manager
ravi.tanaka@verdmont-example.com
www.verdmont-example.com.my
- Pumping technology
- Valve & actuation
- Air moving technology
Target Market(s)
engineers, purchasing managers
Industry/Entity Type
Business
Contact Information for Business Card
Ravi Tanaka
Business manager
ravi.tanaka@verdmont-example.com
www.verdmont-example.com.my
- Pumping technology
- Valve & actuation
- Air moving technology
catch phrase : "Solving flow challenges, exceeding expectations"

```html
<!DOCTYPE html>
<html lang="en">
<head>
<meta charset="utf-8">
<title>Verdmont Flow Solutions – Business Card</title>
<link rel="stylesheet" href="https://fonts.googleapis.com/css2?family=Roboto+Condensed:ital,wght@0,300;0,400;0,700;1,300&display=swap">
<style>
  :root {
    --navy: #0d3144;
    --orange: #f39a2c;
    --paper: #ffffff;
    --grey-text: #8a9197;
    --stage: #4a4a4a;
    --brand-muted: #4a8aa3;
  }
  html, body {
    margin: 0;
    width: 1200px;
    height: 1200px;
    overflow: hidden;
    background: var(--stage);
  }
  .card {
    position: absolute;
    left: 200px;
    width: 800px;
    height: 454px;
    display: block;
    box-shadow: 0 6px 18px rgba(0,0,0,0.45);
  }
  .card--front { top: 115px; }
  .card--back { top: 631px; }
  .card text { font-family: "Roboto Condensed", sans-serif; }
  .brand-name { font-weight: 400; font-size: 40px; fill: var(--navy); letter-spacing: 1px; }
  .brand-name--back { fill: var(--brand-muted); }
  .tagline { font-weight: 300; font-size: 22px; fill: var(--grey-text); }
  .contact { font-weight: 400; font-size: 26px; fill: var(--paper); }
  .person-name { font-weight: 700; font-size: 38px; fill: var(--orange); }
  .person-title { font-weight: 400; font-size: 26px; fill: var(--paper); }
  .product { font-weight: 300; font-style: italic; font-size: 26px; fill: var(--navy); }
</style>
</head>
<body>

<svg class="card card--front" viewBox="0 0 1000 567" preserveAspectRatio="none" aria-label="Business card front">
  <rect class="card-paper" width="1000" height="567" fill="var(--paper)"/>

  <g class="brand">
    <circle cx="88" cy="107" r="42" fill="var(--navy)"/>
    <text class="brand-name" x="150" y="122">Verdmont Flow Solutions</text>
  </g>

  <g class="tagline-block" text-anchor="end">
    <text class="tagline" x="920" y="104">SOLVING FLOW CHALLENGES,</text>
    <text class="tagline" x="920" y="133">EXCEEDING EXPECTATIONS</text>
  </g>

  <g class="band">
    <polygon points="0,197 498,197 608,265 1000,265 1000,468 608,468 498,401 0,401" fill="var(--navy)"/>
    <polyline points="0,223 487,223" fill="none" stroke="var(--orange)" stroke-width="1.5"/>
    <polyline points="487,223 640,322" fill="none" stroke="#3c6478" stroke-width="1"/>
    <polyline points="460,333 615,433" fill="none" stroke="#3c6478" stroke-width="1"/>
    <polyline points="615,433 1000,433" fill="none" stroke="var(--orange)" stroke-width="1.5"/>
  </g>

  <g class="contact-icons" fill="var(--orange)">
    <g class="icon-phone">
      <path d="M73,268 q13,-12 26,0 l-3,6 h-4 l-1,-4 q-7,-3 -10,0 l-1,4 h-4 z"/>
      <rect x="78" y="272" width="16" height="8" rx="2"/>
    </g>
    <g class="icon-mail">
      <rect x="74" y="296" width="24" height="16"/>
      <polyline points="74,296 86,306 98,296" fill="none" stroke="var(--navy)" stroke-width="2"/>
    </g>
    <g class="icon-web" fill="none" stroke="var(--orange)" stroke-width="1.8">
      <circle cx="86" cy="338" r="11"/>
      <ellipse cx="86" cy="338" rx="5" ry="11"/>
      <line x1="75" y1="338" x2="97" y2="338"/>
      <line x1="77" y1="332" x2="95" y2="332"/>
      <line x1="77" y1="344" x2="95" y2="344"/>
    </g>
  </g>

  <g class="contact-list">
    <text class="contact" x="112" y="281">xxx-xxx-xxxx</text>
    <text class="contact" x="112" y="314">ravi.tanaka@verdmont-example.com</text>
    <text class="contact" x="112" y="348">www.verdmont-example.com.my</text>
  </g>

  <g class="person" text-anchor="end">
    <text class="person-name" x="920" y="366">Ravi Tanaka</text>
    <text class="person-title" x="920" y="401">Business manager</text>
  </g>

  <g class="products">
    <text class="product" x="57" y="447">- Pumping technology</text>
    <text class="product" x="57" y="480">- Valve &amp; Actuation</text>
    <text class="product" x="57" y="514">- Air moving technology</text>
  </g>
</svg>

<svg class="card card--back" viewBox="0 0 1000 567" preserveAspectRatio="none" aria-label="Business card back">
  <rect class="card-paper" width="1000" height="567" fill="var(--navy)"/>
  <g class="brand brand--back">
    <circle cx="312" cy="292" r="46" fill="var(--brand-muted)"/>
    <text class="brand-name brand-name--back" x="380" y="308" style="font-size:44px">Verdmont Flow Solutions</text>
  </g>
</svg>

</body>
</html>
```